I need men clothes and shoes selling website

I am a running a small and medium scale business in the United States with deals on the sales of clothes and shoes for men. I am looking for a top quality website to project my business and activities i am relatively new into it. There will be categories for Jeans, Polo, T-shirt, Long sleeves, Short Leaves, sandals, shoes, and slippers. Users would be able to sort category by designers, color and size. I carryout my sales online and only ship to United States and Canada. My website by the name - voranta. I require creativity in the design of the website.

Industry/Entity Type

Business

Coding

Coded - Design and coding required

```html
<!DOCTYPE html>
<html lang="en">
<head>
<meta charset="utf-8">
<title>Voranta – Men's Clothes and Shoes</title>
<link href="https://fonts.googleapis.com/css2?family=PT+Sans:wght@400;700&family=PT+Sans+Narrow:wght@400;700&display=swap" rel="stylesheet">
<style>
:root{
  --black:#111;
  --blue:#4d8ff5;
  --btn:#3b7ff2;
  --btn-edge:#2b64c7;
  --red:#f0141e;
  --grey:#d6d6d6;
  --text:#222;
  --star:#f4a100;
  --line:#cfcfcf;
  --photo-red:#d8232d;
}
*{box-sizing:border-box;margin:0;padding:0}
html,body{width:1120px;height:1200px;overflow:hidden;background:#fff}
body{font-family:"PT Sans",sans-serif;color:var(--text)}
.page{width:1400px;height:1500px;transform:scale(.8);transform-origin:0 0;position:relative;overflow:hidden}
.abs{position:absolute}

/* top bar */
.topbar{left:0;top:0;width:1400px;height:35px;background:var(--black);color:#fff;font-size:13px}
.social{left:258px;top:0;height:35px;display:flex}
.social span{width:30px;height:35px;border-left:1px solid #333;display:flex;align-items:center;justify-content:center}
.social span:last-child{border-right:1px solid #333}
.social i{width:9px;height:9px;border-radius:50%;background:#ddd;display:block}
.top-links{right:60px;top:0;height:35px;display:flex;align-items:center}
.top-links .item{display:flex;align-items:center;gap:8px}
.top-links .track{margin-right:44px}
.flag{width:18px;height:12px;background:#1d3b8f;position:relative;overflow:hidden}
.flag:before{content:"";position:absolute;left:7px;top:0;width:4px;height:12px;background:#e33}
.flag:after{content:"";position:absolute;left:0;top:4px;width:18px;height:4px;background:#e33}
.top-links .lang{margin-right:46px}
.sep{margin:0 14px}

/* header */
.logo{left:60px;top:62px;font-family:"PT Sans Narrow",sans-serif;font-weight:700;font-size:50px;color:var(--red);line-height:1}
.support{left:250px;top:60px;display:flex;align-items:center;gap:6px}
.support .t1{font-size:14px;letter-spacing:.3px;padding-left:14px}
.support .t2{font-size:19px;font-family:"PT Sans Narrow",sans-serif}
.search{left:478px;top:63px;width:570px;height:50px;border:1px solid #bbb;display:flex}
.search .field{flex:1;padding:0 20px;display:flex;align-items:center;font-size:14px;border-right:1px solid #bbb}
.search .cat{width:194px;padding:0 10px 0 20px;display:flex;align-items:center;justify-content:space-between;font-size:14px}
.search .cat b{color:#bbb;font-size:11px}
.search .go{width:46px;background:var(--red);display:flex;align-items:center;justify-content:center}
.reco{right:62px;top:72px;text-align:right;font-size:13px;line-height:18px}

/* nav */
.nav{left:0;top:120px;width:1400px;height:50px;background:var(--blue);color:#fff}
.crumb{left:62px;top:16px;font-size:13px;letter-spacing:2.5px;font-weight:700}
.menu{left:624px;top:0;height:50px;display:flex;align-items:center;font-size:14px}
.menu .num{font-size:18px}
.menu .ic{display:flex;align-items:center;gap:5px}

/* sidebar deals */
.deal{left:60px;width:260px;height:420px;background:var(--grey)}
.deal h3{position:absolute;left:15px;top:14px;font-weight:400;font-size:19px;letter-spacing:.5px}
.arrows{position:absolute;left:193px;top:14px;display:flex;gap:2px}
.arrows span{width:24px;height:26px;background:#fff;color:#bbb;font-size:13px;display:flex;align-items:center;justify-content:center}
.deal .pic{position:absolute;left:16px;top:50px;width:228px;height:204px;background:radial-gradient(ellipse at center,#4a3f38 0%,#8a7e76 35%,#fff 70%)}
.deal .price{position:absolute;left:20px;top:272px;font-size:46px;font-weight:700;color:var(--red);line-height:1}
.deal .price sup{font-size:20px;vertical-align:top;line-height:1.3}
.deal .info{position:absolute;left:149px;top:278px;font-size:14px;color:var(--red);line-height:18px}
.deal .info .name{font-family:"PT Sans Narrow",sans-serif;font-size:16px}
.deal .btn{position:absolute;left:48px;top:360px}
.deal .heart{position:absolute;left:206px;top:376px}

/* categories */
.cat-title{left:81px;top:652px;font-size:19px;letter-spacing:.8px}
.cats{left:60px;top:686px;width:260px}
.cats li{list-style:none;height:50px;background:var(--grey);margin-bottom:1px;padding:0 20px 0 36px;display:flex;align-items:center;justify-content:space-between;font-size:16px;letter-spacing:.8px}
.cats li b{font-size:9px;color:#fff}

/* banner */
.banner{left:345px;top:195px;width:995px;height:420px;background:linear-gradient(90deg,#625a52 0%,#8a8078 30%,#d4d2d0 45%,#dedddd 100%);box-shadow:0 2px 4px rgba(0,0,0,.25)}
.banner .scene{position:absolute;left:20px;top:0;width:440px;height:420px}
.banner .copy{position:absolute;left:485px;top:88px;width:400px;text-align:center}
.copy .pre{font-family:"PT Sans Narrow",sans-serif;font-size:22px;color:#111}
.copy .big{font-weight:700;font-size:50px;letter-spacing:1px;line-height:1;margin-top:2px;color:#111}
.copy .shop{display:inline-block;margin-top:22px;background:#000;color:#fff;font-size:14px;padding:12px 22px;letter-spacing:.5px}
.brands{margin-top:30px;display:flex;justify-content:center;gap:18px;align-items:center;font-size:15px;color:#222}
.brands .b1{font-weight:700;letter-spacing:.5px}
.brands .b3{font-size:19px}
.brands .b4{font-weight:700;font-size:13px}
.round{position:absolute;top:208px;width:48px;height:48px;border-radius:50%;background:#fff;display:flex;align-items:center;justify-content:center}

/* products */
.list-title{left:347px;top:660px;font-size:15px}
.sort{left:1212px;top:661px;font-size:14px;color:#aaa;display:flex;gap:8px;align-items:center}
.sort span{width:20px;height:14px;background:#ddd;display:flex;align-items:center;justify-content:center}
.card{width:232px;height:420px;border:1px solid var(--line);background:#fff}
.card .pic{position:absolute;left:20px;top:8px;width:190px;height:222px;background:radial-gradient(ellipse at center,var(--photo-red) 0%,#e45a60 40%,#fff 72%)}
.tag{position:absolute;left:8px;top:212px;border:1px solid #999;background:#fff;font-size:12px;padding:5px 10px}
.card .price{position:absolute;left:9px;top:250px;font-size:32px;font-weight:700;color:var(--red);line-height:1}
.card .price sup{font-size:15px;vertical-align:top;line-height:1.2}
.card .old{position:absolute;left:10px;top:281px;font-size:24px;font-weight:700;color:#999;line-height:1;text-decoration:line-through}
.card .old sup{font-size:12px;vertical-align:top}
.card .name{position:absolute;left:87px;top:262px;color:var(--red);font-size:16px}
.card .stars{position:absolute;left:87px;top:284px;color:var(--star);font-size:17px;line-height:16px;letter-spacing:1px}
.card .size{position:absolute;left:87px;top:316px;color:var(--red);font-size:15px}
.card .size b{margin-left:5px;margin-right:8px}
.card .btn{position:absolute;left:38px;top:355px}
.card .heart{position:absolute;left:196px;top:366px}
.btn{width:154px;height:46px;background:var(--btn);color:#fff;font-weight:700;font-size:16px;letter-spacing:.8px;display:flex;align-items:center;justify-content:center;box-shadow:inset 0 -4px 0 var(--btn-edge)}
</style>
</head>
<body>
<div class="page">

  <div class="abs topbar">
    <div class="abs social"><span><i></i></span><span><i></i></span><span><i></i></span><span><i></i></span></div>
    <div class="abs top-links">
      <div class="item track"><svg width="8" height="11" viewBox="0 0 8 11"><path d="M4 0a4 4 0 0 0-4 4c0 3 4 7 4 7s4-4 4-7a4 4 0 0 0-4-4z" fill="#fff"/><circle cx="4" cy="4" r="1.5" fill="#111"/></svg> Track Order</div>
      <div class="item lang"><span class="flag"></span> ENG <span style="margin-left:12px;font-size:10px">▼</span></div>
      <div class="item">Login<span class="sep">|</span>Signup</div>
    </div>
  </div>

  <div class="abs logo">VORANTA</div>
  <div class="abs support">
    <svg width="48" height="48" viewBox="0 0 48 48"><circle cx="26" cy="24" r="17" fill="none" stroke="#aaa" stroke-width="3"/><path d="M6 14l6 3-3 6 6 8 5-3 4 5c-5 5-12 2-16-4S2 18 6 14z" fill="#aaa"/><text x="19" y="29" font-family="PT Sans" font-weight="700" font-size="14" fill="#888">24</text></svg>
    <div><div class="t1">Customer Support</div><div class="t2">(000) 321-654 987</div></div>
  </div>
  <div class="abs search">
    <div class="field">Search for Product</div>
    <div class="cat">All Categories <b>▼</b></div>
    <div class="go"><svg width="18" height="18" viewBox="0 0 18 18"><circle cx="7" cy="7" r="5" fill="none" stroke="#fff" stroke-width="2.4"/><path d="M11 11l5 5" stroke="#fff" stroke-width="2.6"/></svg></div>
  </div>
  <div class="abs reco"><u>Signup</u> to get Our<br>personalized Recommendation</div>

  <div class="abs nav">
    <div class="abs crumb"><u>POLO SHIRTS</u> &nbsp;&gt;&nbsp; <u>SLIM FIT</u></div>
    <div class="abs menu">
      <svg width="18" height="16" viewBox="0 0 18 16" style="margin-right:32px"><path d="M9 0L0 8h3v8h4v-5h4v5h4V8h3z" fill="#fff"/></svg>
      <span style="margin-right:48px">CATEGORIES ▾</span>
      <span style="margin-right:100px">CONTACT US</span>
      <span class="ic" style="margin-right:34px"><svg width="18" height="16" viewBox="0 0 18 16"><path d="M9 15S1 10 1 5a4 4 0 0 1 8-1 4 4 0 0 1 8 1c0 5-8 10-8 10z" fill="#f0141e"/></svg><span class="num">0</span></span>
      <span class="ic" style="margin-right:38px"><span style="color:var(--star);font-size:17px">★</span><span class="num">0</span></span>
      <span class="ic" style="margin-right:48px"><svg width="18" height="16" viewBox="0 0 18 16"><path d="M0 1h3l3 9h9l2-7H5" fill="none" stroke="#fff" stroke-width="2"/><circle cx="7" cy="14" r="1.6" fill="#fff"/><circle cx="14" cy="14" r="1.6" fill="#fff"/></svg><span class="num">0.00$</span></span>
      <span class="ic">CHECKOUT <svg width="22" height="16" viewBox="0 0 22 16"><path d="M0 1h3l3 9h9l2-7H5" fill="none" stroke="#fff" stroke-width="2"/><circle cx="7" cy="14" r="1.6" fill="#fff"/><circle cx="14" cy="14" r="1.6" fill="#fff"/><path d="M19 4l3 4-3 4z" fill="#fff"/></svg></span>
    </div>
  </div>

  <div class="abs deal" style="top:195px">
    <h3>Best Deals</h3>
    <div class="arrows"><span>&lt;</span><span>&gt;</span></div>
    <div class="pic" role="img" aria-label="Dark brown leather sandal with ankle strap"></div>
    <div class="price">258<sup>$</sup></div>
    <div class="info"><div class="name">TRK Sandals</div><div style="color:var(--star)">★★★★<span style="opacity:.5">★</span></div><div>Size: &nbsp;9”</div><div>Posted: 4 Sept</div></div>
    <div class="btn">Add to cart</div>
    <svg class="heart" width="18" height="16" viewBox="0 0 18 16"><path d="M9 15S1 10 1 5a4 4 0 0 1 8-1 4 4 0 0 1 8 1c0 5-8 10-8 10z" fill="none" stroke="#fff" stroke-width="1.4"/></svg>
  </div>

  <div class="abs cat-title">Main Categories</div>
  <ul class="abs cats">
    <li>Jeans<b>▶</b></li><li>Polo<b>▶</b></li><li>T-shirt<b>▶</b></li><li>Long sleeves<b>▶</b></li><li>Short Leaves<b>▶</b></li><li>sandals<b>▶</b></li><li>shoes<b>▶</b></li>
  </ul>

  <div class="abs deal" style="top:1065px">
    <h3>Best Deals</h3>
    <div class="arrows"><span>&lt;</span><span>&gt;</span></div>
    <div class="pic" role="img" aria-label="Dark brown leather sandal with ankle strap"></div>
    <div class="price">258<sup>$</sup></div>
    <div class="info"><div class="name">TRK Sandals</div><div style="color:var(--star)">★★★★<span style="opacity:.5">★</span></div><div>Size: &nbsp;9”</div><div>Posted: 4 Sept</div></div>
  </div>

  <div class="abs banner">
    <div class="scene" role="img" aria-label="Turquoise polo shirt, hiking shoes and a young man in a raglan tee and dark jeans"></div>
    <div class="round" style="left:7px"><svg width="14" height="24" viewBox="0 0 14 24"><path d="M12 2L2 12l10 10" fill="none" stroke="#333" stroke-width="2"/></svg></div>
    <div class="round" style="left:940px"><svg width="14" height="24" viewBox="0 0 14 24"><path d="M2 2l10 10L2 22" fill="none" stroke="#333" stroke-width="2"/></svg></div>
    <div class="copy">
      <div class="pre">WELCOME THE NEW SEASON WITH THESE</div>
      <div class="big">NEW ARRIVALS</div>
      <div class="shop">SHOP NOW</div>
      <div class="brands"><span class="b1">LUMEN ROW</span><span>Soleil</span><span class="b3">halden</span><span class="b4">CARVER &amp; FINN</span></div>
    </div>
  </div>

  <div class="abs list-title">Polo Tops</div>
  <div class="abs sort">Sort <span style="margin-left:24px"><svg width="10" height="6"><path d="M0 0h10L5 6z" fill="#fff"/></svg></span><span><svg width="10" height="6"><path d="M0 6h10L5 0z" fill="#fff"/></svg></span></div>

  <div class="abs card" style="left:345px;top:685px"><div class="pic" role="img" aria-label="Photo of a red slim fit polo shirt"></div><div class="tag">New</div><div class="price">299<sup>$</sup></div><div class="old">399<sup>$</sup></div><div class="name">Slim Fit Polo</div><div class="stars">★★★★★</div><div class="size">Size:<b>M</b><b>L</b><b>XL</b></div><div class="btn">Add to cart</div><svg class="heart" width="18" height="16" viewBox="0 0 18 16"><path d="M9 15S1 10 1 5a4 4 0 0 1 8-1 4 4 0 0 1 8 1c0 5-8 10-8 10z" fill="none" stroke="#ccc" stroke-width="1.4"/></svg></div>
  <div class="abs card" style="left:599px;top:685px"><div class="pic" role="img" aria-label="Photo of a red slim fit polo shirt"></div><div class="price">299<sup>$</sup></div><div class="old">399<sup>$</sup></div><div class="name">Slim Fit Polo</div><div class="stars">★★★★★</div><div class="size">Size:<b>M</b><b>L</b><b>XL</b></div><div class="btn">Add to cart</div><svg class="heart" width="18" height="16" viewBox="0 0 18 16"><path d="M9 15S1 10 1 5a4 4 0 0 1 8-1 4 4 0 0 1 8 1c0 5-8 10-8 10z" fill="none" stroke="#ccc" stroke-width="1.4"/></svg></div>
  <div class="abs card" style="left:853px;top:685px"><div class="pic" role="img" aria-label="Photo of a red slim fit polo shirt"></div><div class="price">299<sup>$</sup></div><div class="old">399<sup>$</sup></div><div class="name">Slim Fit Polo</div><div class="stars">★★★★★</div><div class="size">Size:<b>M</b><b>L</b><b>XL</b></div><div class="btn">Add to cart</div><svg class="heart" width="18" height="16" viewBox="0 0 18 16"><path d="M9 15S1 10 1 5a4 4 0 0 1 8-1 4 4 0 0 1 8 1c0 5-8 10-8 10z" fill="none" stroke="#ccc" stroke-width="1.4"/></svg></div>
  <div class="abs card" style="left:1107px;top:685px"><div class="pic" role="img" aria-label="Photo of a red slim fit polo shirt"></div><div class="tag">New</div><div class="price">299<sup>$</sup></div><div class="old">399<sup>$</sup></div><div class="name">Slim Fit Polo</div><div class="stars">★★★★★</div><div class="size">Size:<b>M</b><b>L</b><b>XL</b></div><div class="btn">Add to cart</div><svg class="heart" width="18" height="16" viewBox="0 0 18 16"><path d="M9 15S1 10 1 5a4 4 0 0 1 8-1 4 4 0 0 1 8 1c0 5-8 10-8 10z" fill="none" stroke="#ccc" stroke-width="1.4"/></svg></div>

  <div class="abs card" style="left:345px;top:1127px"><div class="pic" role="img" aria-label="Photo of a red slim fit polo shirt"></div><div class="price">299<sup>$</sup></div><div class="old">399<sup>$</sup></div><div class="name">Slim Fit Polo</div><div class="stars">★★★★★</div><div class="size">Size:<b>M</b><b>L</b><b>XL</b></div><div class="btn">Add to cart</div></div>
  <div class="abs card" style="left:599px;top:1127px"><div class="pic" role="img" aria-label="Photo of a red slim fit polo shirt"></div><div class="tag">New</div><div class="price">299<sup>$</sup></div><div class="old">399<sup>$</sup></div><div class="name">Slim Fit Polo</div><div class="stars">★★★★★</div><div class="size">Size:<b>M</b><b>L</b><b>XL</b></div><div class="btn">Add to cart</div></div>
  <div class="abs card" style="left:853px;top:1127px"><div class="pic" role="img" aria-label="Photo of a red slim fit polo shirt"></div><div class="tag">New</div><div class="price">299<sup>$</sup></div><div class="old">399<sup>$</sup></div><div class="name">Slim Fit Polo</div><div class="stars">★★★★★</div><div class="size">Size:<b>M</b><b>L</b><b>XL</b></div><div class="btn">Add to cart</div></div>
  <div class="abs card" style="left:1107px;top:1127px"><div class="pic" role="img" aria-label="Photo of a red slim fit polo shirt"></div><div class="price">299<sup>$</sup></div><div class="old">399<sup>$</sup></div><div class="name">Slim Fit Polo</div><div class="stars">★★★★★</div><div class="size">Size:<b>M</b><b>L</b><b>XL</b></div><div class="btn">Add to cart</div></div>

</div>
</body>
</html>
```